Business Card for Voltrix

Horizontal business card for voltrix, the electrical contractor.
clean and professional looking, using company branding and colours.
I also want the blue in the logo and wording to be made a more 'electric' blue and the grey 'Voltrix' to be slightly darker.

Pleas use the following contact details:

Colin Marsh
Owner

t: 01736 582910
m: 07831 206719
e: colin@voltrix-installs.co.uk

www.voltrix-installs.co.uk

Industry/Entity Type

Electrical

Font styles to use
Sans Serif

```html
<!DOCTYPE html>
<html lang="en">
<head>
<meta charset="utf-8">
<title>Voltrix – Business Card</title>
<link href="https://fonts.googleapis.com/css2?family=Michroma&family=Tinos&display=swap" rel="stylesheet">
<style>
  :root {
    --deep-blue: #0a2f8c;
    --mid-blue: #1a5fd0;
    --electric-blue: #19a8ff;
    --mark-teal: #3fd6e0;
    --mark-grey: #45484d;
    --brand-grey: #8a8d90;
    --text-white: #ffffff;
  }
  html, body {
    margin: 0;
    padding: 0;
    width: 1200px;
    height: 640px;
    overflow: hidden;
    background: #ffffff;
  }
  .card {
    position: relative;
    width: 1200px;
    height: 640px;
    overflow: hidden;
    background: linear-gradient(160deg, var(--deep-blue) 0%, var(--mid-blue) 45%, var(--electric-blue) 100%);
    font-family: "Tinos", "Times New Roman", serif;
    color: var(--text-white);
  }
  .card p, .card h1 { margin: 0; }
  .card__artwork {
    position: absolute;
    inset: 0;
    background:
      radial-gradient(ellipse 55% 14% at 50% 50%, rgba(207,228,255,0.55) 0%, rgba(120,170,255,0.25) 55%, rgba(0,0,0,0) 100%),
      radial-gradient(circle at 60px 330px, rgba(130,130,150,0.55) 0 70px, rgba(0,0,0,0) 72px),
      radial-gradient(circle at 1140px 330px, rgba(130,130,150,0.55) 0 70px, rgba(0,0,0,0) 72px),
      linear-gradient(175deg, rgba(0,0,0,0) 60%, rgba(120,210,255,0.35) 80%, rgba(0,0,0,0) 100%);
  }
  .brand-name {
    position: absolute;
    left: 20px;
    top: 4px;
    width: 1160px;
    height: 110px;
  }
  .brand-name text {
    font-family: "Michroma", "Arial", sans-serif;
    font-size: 112px;
    fill: var(--brand-grey);
  }
  .brand-mark {
    position: absolute;
    left: 0;
    right: 0;
    top: 240px;
    display: flex;
    justify-content: center;
    align-items: center;
    gap: 22px;
  }
  .brand-mark__dot {
    width: 100px;
    height: 100px;
    border-radius: 50%;
    background: var(--mark-teal);
  }
  .brand-mark__name {
    font-family: "Michroma", "Arial", sans-serif;
    font-size: 46px;
    color: var(--mark-grey);
    line-height: 1;
  }
  .contact {
    position: absolute;
    font-size: 30px;
    line-height: 1;
    white-space: nowrap;
  }
  .contact--email { left: 12px; top: 118px; }
  .contact--phone { left: 12px; top: 600px; }
  .contact--mobile { right: 12px; top: 600px; }
  .contact--web { left: 0; right: 0; top: 572px; text-align: center; }
  .person {
    position: absolute;
    right: 8px;
    top: 132px;
    text-align: center;
    font-size: 36px;
    line-height: 1.4;
  }
  .tagline {
    position: absolute;
    left: 0;
    right: 0;
    top: 476px;
    text-align: center;
    font-family: "Michroma", "Arial", sans-serif;
    font-size: 30px;
    font-weight: normal;
    letter-spacing: 2px;
    color: var(--text-white);
  }
</style>
</head>
<body>
  <main class="card">
    <div class="card__artwork" role="img" aria-label="Electric arcs of lightning crackling between two grey insulator coils on a blue tiled background"></div>

    <svg class="brand-name" viewBox="0 0 1160 110" aria-label="Voltrix">
      <text x="0" y="100" textLength="1160" lengthAdjust="spacingAndGlyphs">VOLTRIX</text>
    </svg>

    <p class="contact contact--email">e: colin@voltrix-installs.co.uk</p>

    <div class="person">
      <p class="person__name">Colin Marsh</p>
      <p class="person__role">Owner</p>
    </div>

    <div class="brand-mark">
      <span class="brand-mark__dot"></span>
      <span class="brand-mark__name">VOLTRIX</span>
    </div>

    <h1 class="tagline">THE ELECTRICAL CONTRACTOR</h1>

    <p class="contact contact--web">www.voltrix-installs.co.uk</p>
    <p class="contact contact--phone">t: 01736 582910</p>
    <p class="contact contact--mobile">m: 07831 206719</p>
  </main>
</body>
</html>
```